Professional Modern Website Design

We are a premium IT services provider to the financial industry based in London. Our company is called Veltra our current holding page is www.veltra-example.co.uk. We require a new website to match our new corporate identity. This project is for the design phase only. Development will be handled in-house. I have attached examples of wire frames we have developed (although open to suggestions for improvement) Our brand document that should demonstrate current brand, inc how we communicate to potential clients and finally mostly completed web-content.
We are looking for designers that can create something that sets us apart from our competitors.
Target Market(s)
IT Decision makers in Finance companies such as; hedge funds, private investment banks etc
Industry/Entity Type
Financial
Number of Pages Required
5+ page
Requirements
Must have
- hexagon elements in the design, unique design.
Nice to have
- Blog and social media feeds
Should not have
- Should not resemble a downloaded template

```html
<!DOCTYPE html>
<html lang="en">
<head>
<meta charset="utf-8">
<title>Veltra — Systems Integration for Finance</title>
<link rel="stylesheet" href="https://fonts.googleapis.com/css2?family=Open+Sans:wght@400;600;700&family=Roboto:wght@300;400;700&family=Roboto+Condensed:wght@400&display=swap">
<style>
:root{
  --ink:#2b2b2b;
  --ink-deep:#1b1b1b;
  --orange:#f05a28;
  --orange-warm:#f3832a;
  --orange-base:#d9782e;
  --grey-a:#e3e3e3;
  --text:#555;
  --white:#fff;
  --field:#6e6e6e;
  --hex:polygon(25% 3%,75% 3%,100% 50%,75% 97%,25% 97%,0 50%);
}
*{box-sizing:border-box;margin:0;padding:0}
html,body{width:702px;height:1200px;overflow:hidden;background:var(--white)}
body{position:relative;font-family:"Open Sans",Arial,sans-serif;color:var(--text)}

/* header */
.site-header{position:absolute;left:0;top:0;width:702px;height:66px;background:var(--ink)}
.brand{position:absolute;left:28px;top:9px;display:flex;flex-direction:column;align-items:flex-start;gap:6px}
.brand-mark{width:34px;height:34px;background:var(--orange)}
.brand-name{font-family:"Roboto",Arial,sans-serif;font-size:8px;letter-spacing:3px;color:#bbb}
.main-nav{position:absolute;left:272px;top:0;display:flex;height:43px;align-items:flex-end;font-family:"Roboto",Arial,sans-serif;font-size:6.6px;color:var(--white)}
.main-nav a{color:inherit;text-decoration:none;padding:0 9px 8px;position:relative}
.main-nav a.active{background:var(--orange);height:43px;display:flex;align-items:flex-end;width:40px;justify-content:center;padding:0 0 8px}
.main-nav a+a:not(.first)::before{content:"";position:absolute;left:0;bottom:8px;width:1px;height:7px;background:var(--orange)}

/* hero */
.hero{position:absolute;left:0;top:66px;width:702px;height:239px;background:linear-gradient(90deg,#fafafa 0%,#f2f2f2 40%,#e6e6e6 100%);overflow:hidden}
.hero-visual{position:absolute;left:150px;top:0;width:552px;height:239px;background:radial-gradient(circle at 57% 62%,rgba(240,110,40,.85) 0,rgba(240,110,40,.35) 9%,transparent 16%),radial-gradient(ellipse at 70% 40%,#bfbfbf 0%,#e4e4e4 55%,rgba(242,242,242,0) 80%)}
.hero-title{position:absolute;left:27px;top:36px;font-family:"Roboto",Arial,sans-serif;font-size:18px;line-height:17.5px;font-weight:300;color:#333;letter-spacing:-.3px}
.hero-title strong{display:block;font-weight:700;color:var(--orange)}
.hero-copy{position:absolute;left:27px;top:112px;width:216px;font-size:6.3px;line-height:9.6px;color:#333;text-transform:uppercase}
.btn-more{position:absolute;left:27px;top:162px;width:85px;height:22px;background:var(--orange);border-radius:3px;color:var(--white);font-size:8.4px;font-weight:600;display:flex;align-items:center;justify-content:center}

/* audience */
.audience{position:absolute;left:0;top:305px;width:702px;height:265px;background:var(--grey-a)}
.audience-bg{position:absolute;left:0;top:0}
.section-title{position:absolute;left:0;width:702px;text-align:center;font-family:"Roboto",Arial,sans-serif;font-weight:300;color:var(--white)}
.audience .section-title{top:20px;font-size:18px}
.audience-lead{position:absolute;left:0;top:45px;width:702px;text-align:center;font-size:8px;font-weight:600;color:#333}
.persona{position:absolute;top:72px;width:128px}
.persona h3{font-family:"Roboto",Arial,sans-serif;font-weight:300;font-size:12px;line-height:12px;color:var(--orange);height:24px;display:flex;align-items:flex-end;margin-bottom:12px}
.persona p{font-size:6.9px;line-height:12px;color:var(--text)}

/* services */
.services{position:absolute;left:0;top:570px;width:702px;height:274px;background:var(--orange-base);overflow:hidden}
.services-bg{position:absolute;left:0;top:0}
.services-heading{position:absolute;left:42px;top:41px;width:618px;display:flex;align-items:center;gap:8px;color:var(--white);font-family:"Roboto",Arial,sans-serif;font-weight:300;font-size:13px}
.services-heading .rule{flex:1;height:3px;border-top:1px solid var(--white);border-bottom:1px solid var(--white)}
.services-lead{position:absolute;left:0;top:65px;width:702px;text-align:center;font-family:"Roboto Condensed",Arial,sans-serif;font-weight:400;font-size:8px;color:var(--white)}
.service{position:absolute;top:90px;width:110px;color:var(--white)}
.service-image{position:relative;width:110px;height:67px}
.service-image.datacentre{background:linear-gradient(160deg,#9a9a9a,#1f1f1f)}
.service-image.support{background:linear-gradient(160deg,#b9ccdc,#4b6b88)}
.service-image.voice{background:linear-gradient(160deg,#5c6b7c,#1e2a38)}
.service-image.cloud{background:linear-gradient(160deg,#1d6fb3,#0d1d3c)}
.service-image.security{background:linear-gradient(160deg,#3f5f86,#101a2c)}
.service-label{position:absolute;left:0;bottom:0;width:110px;height:27px;background:rgba(20,20,20,.75);display:flex;align-items:center;justify-content:center;text-align:center;font-family:"Roboto Condensed",Arial,sans-serif;font-size:8px;line-height:9px}
.service p{margin-top:6px;font-size:6.8px;line-height:9.2px;height:58px}
.service a{font-size:6.4px;font-weight:700;color:var(--white);text-decoration:underline}

/* social */
.social{position:absolute;left:0;top:844px;width:702px;height:39px;background:var(--ink);display:flex;justify-content:center;align-items:center;gap:9px}
.social-hex{width:20px;height:18px;background:#8d8d8d;clip-path:var(--hex)}

/* contact */
.contact{position:absolute;left:0;top:883px;width:702px;height:281px;background:radial-gradient(ellipse at 75% 80%,#5a5a5a 0%,#3a3a3a 55%,#2c2c2c 100%)}
.contact .section-title{top:20px;font-size:14px}
.contact-lead{position:absolute;left:0;top:38px;width:702px;text-align:center;font-family:"Roboto",Arial,sans-serif;font-size:8.6px;color:#e6e6e6}
.offices{position:absolute;left:30px;top:69px;width:320px;height:147px;background:rgba(30,30,30,.75)}
.office{position:absolute;font-family:"Roboto",Arial,sans-serif;font-size:6.2px;line-height:10.4px;color:#9a9a9a;text-transform:uppercase}
.office h4{font-family:"Roboto Condensed",Arial,sans-serif;font-weight:400;font-size:8px;color:var(--orange);line-height:11px}
.office .phone{font-family:"Roboto Condensed",Arial,sans-serif;font-size:8px;color:var(--orange)}
.contact-form{position:absolute;left:380px;top:73px;width:292px}
.field{position:absolute;left:0;width:292px;display:flex;align-items:flex-start}
.field label{width:92px;text-align:right;padding-right:8px;font-family:"Roboto",Arial,sans-serif;font-size:7.6px;color:#f0f0f0;padding-top:4px}
.field span{display:block;width:200px;height:20px;background:var(--field)}
.field.message span{height:54px}
.btn-send{position:absolute;display:flex;align-items:center;justify-content:center;background:var(--orange);color:var(--white);font-family:"Roboto",Arial,sans-serif;font-size:7.6px}

/* footer */
.site-footer{position:absolute;left:0;top:1164px;width:702px;height:36px;background:var(--ink-deep)}
.subscribe-label{position:absolute;left:154px;top:12px;font-family:"Roboto",Arial,sans-serif;font-size:8.4px;color:#e6e6e6}
.subscribe-input{position:absolute;left:256px;top:10px;width:200px;height:17px;background:var(--white);font-family:"Roboto",Arial,sans-serif;font-size:6.8px;color:#bbb;padding:4px 7px}
</style>
</head>
<body>

<header class="site-header">
  <div class="brand">
    <span class="brand-mark"></span>
    <span class="brand-name">VELTRA</span>
  </div>
  <nav class="main-nav">
    <a class="active first" href="#">HOME</a>
    <a class="first" href="#">ABOUT US</a>
    <a href="#">SERVICES</a>
    <a href="#">DATA CENTRE &amp; INFRASTRUCTURE</a>
    <a href="#">TESTIMONIAL</a>
    <a href="#">CONTACT US</a>
  </nav>
</header>

<section class="hero">
  <div class="hero-visual" role="img" aria-label="Network of chrome spheres joined by steel rods, one orange sphere at the centre"></div>
  <h1 class="hero-title">YOU NEED<br>INTEGRATION.<strong>WE’RE ALWAYS<br>THERE WITH YOU.</strong></h1>
  <p class="hero-copy">Veltra is one of the leading systems integrators to the world’s finance sector. We are an extension of your business and our services portfolio has been built so you always have access to a complete partner.</p>
  <a class="btn-more">MORE INO</a>
</section>

<section class="audience">
  <svg class="audience-bg" width="702" height="265" viewBox="0 0 702 265" aria-hidden="true">
    <rect x="0" y="0" width="175" height="265" fill="#e3e3e3"/>
    <rect x="175" y="0" width="175" height="265" fill="#ebebeb"/>
    <rect x="350" y="0" width="176" height="265" fill="#e3e3e3"/>
    <rect x="526" y="0" width="176" height="265" fill="#eeeeee"/>
    <polygon points="210,0 350,0 350,82" fill="#ea5a2a"/>
    <polygon points="350,0 492,0 350,82" fill="#eb7b2c"/>
  </svg>
  <h2 class="section-title">Who Are You?</h2>
  <p class="audience-lead">If you’re part of a financial organisation, we have the power to help everyone work more efficiently, productively and profitably.</p>
  <article class="persona" style="left:29px">
    <h3>Senior Hedge<br>Fund Manager/CEO</h3>
    <p>You need to develop and implement strategies for business growth, while ensuring profitability. You’re aware your biggest asset is your staff and a happy workforce is a productive one. Security is a key concern in a changing always-on world and you need to be compliant, but you don’t want to overspend. Veltra can help you find the best solutions to help your business grow at the speed you want it to.</p>
  </article>
  <article class="persona" style="left:203px">
    <h3>CFO</h3>
    <p>Your key responsibility is to obtain the maximum ROI from products and services. You understand investment opportunities, providing they return higher efficiencies and revenues. You are concerned more with long-term spending versus short-term and how you can get the most value out of a proposition. Veltra can advise how to boost ROI by streamlining your business to maximise return.</p>
  </article>
  <article class="persona" style="left:373px">
    <h3>IT Manager/CTO</h3>
    <p>Integration with partners and services is your key concern. You want to make sure any IT system you implement will work with the whole infrastructure of your company. You don’t want your team to waste valuable time dealing with things that don’t matter. Veltra provides the whole picture to ensure your company is ready for the next generation of IT.</p>
  </article>
  <article class="persona" style="left:549px;top:66px;width:128px">
    <h3>Employees</h3>
    <p>You’re working hard, but not getting anywhere fast. You want the tools to make your job easier so you can spend more time thinking about what you’re doing rather than how you’re doing it. You shouldn’t have to think about the technology you’re using, because it should just work. Veltra can help you get back on track everyday.</p>
  </article>
</section>

<section class="services">
  <svg class="services-bg" width="702" height="274" viewBox="0 0 702 274" aria-hidden="true">
    <rect width="702" height="274" fill="#d9782e"/>
    <polygon points="0,0 180,0 0,72" fill="#ee5f2a"/>
    <polygon points="180,0 350,0 350,274" fill="#f05a28"/>
    <polygon points="350,0 524,0 350,274" fill="#f3832a"/>
    <polygon points="524,0 702,0 702,72" fill="#f3832a"/>
  </svg>
  <div class="services-heading"><span class="rule"></span><span>OUR SERVICES</span><span class="rule"></span></div>
  <p class="services-lead">We are a world-class systems integrator with a wide range of expertise within the technology market, with no sector left unexplored.</p>

  <article class="service" style="left:42px">
    <div class="service-image datacentre" role="img" aria-label="Rows of server racks in a data centre">
      <span class="service-label">DATA CENTRE &amp;<br>INFRASTRUCTURE</span>
    </div>
    <p>Veltra offers analysis, assessment, implementation and management of your infrastructure to boost your company’s productivity and profitability.</p>
    <a href="#">more...</a>
  </article>
  <article class="service" style="left:170px">
    <div class="service-image support" role="img" aria-label="Small business figures standing on a connected network grid">
      <span class="service-label">IT Support, Managed &amp;<br>Professional Services</span>
    </div>
    <p>Veltra built its reputation on IT support, managed and professional services and it continues to operate with these as a priority.</p>
    <a href="#">more...</a>
  </article>
  <article class="service" style="left:297px">
    <div class="service-image voice" role="img" aria-label="Network patch panel with blue cables">
      <span class="service-label">Voice &amp;<br>Data Networks</span>
    </div>
    <p>Veltra can offer hosted Voice over IP (VoIP) and more traditional PBX systems based around a flexible, mobile and agile platform.</p>
    <a href="#">more...</a>
  </article>
  <article class="service" style="left:424px">
    <div class="service-image cloud" role="img" aria-label="Glowing blue cloud over streams of binary code">
      <span class="service-label">Hosting &amp; Cloud</span>
    </div>
    <p>Veltra can help companies adopt a highly secure hosting and cloud solution to keep data safe and processes efficient</p>
    <a href="#">more...</a>
  </article>
  <article class="service" style="left:550px">
    <div class="service-image security" role="img" aria-label="Keys resting on a keyboard in blue light">
      <span class="service-label">IT Security &amp; IRM</span>
    </div>
    <p>Veltra offers specialised information risk and IT security management. We know how important protection is and your whole organisation should too.</p>
    <a href="#">more...</a>
  </article>
</section>

<nav class="social" aria-label="Social media">
  <span class="social-hex" aria-label="Social profile 1"></span>
  <span class="social-hex" aria-label="Social profile 2"></span>
  <span class="social-hex" aria-label="Social profile 3"></span>
  <span class="social-hex" aria-label="Social profile 4"></span>
  <span class="social-hex" aria-label="Social profile 5"></span>
</nav>

<section class="contact" role="region" aria-label="Contact us, background of a desk with calculator and papers in grey tones">
  <h2 class="section-title">CONTACT US</h2>
  <p class="contact-lead">Have your people get in touch with our people.</p>

  <div class="offices">
    <div class="office" style="left:20px;top:19px">
      <h4>LONDON OFFICE</h4>
      18 Harlow Mews,<br>Mayfair, London W1X 2QT<br>T: +44 20 7946 0812<br>E: info@veltra-example.co.uk
    </div>
    <div class="office" style="left:179px;top:19px">
      <h4>ESSEX OFFICE</h4>
      9 Elmfield Works, Elmfield Lane<br>Southend, Essex SS9 4RB<br>T: +44 20 7946 0812<br>E: info@veltra-example.co.uk
    </div>
    <div class="office" style="left:20px;top:101px">
      <h4>SUPPORT:</h4>
      <span class="phone">T: +44 20 7946 0813</span>
    </div>
    <div class="office" style="left:178px;top:101px">
      <h4>SALES:</h4>
      <span class="phone">T: +44 20 7946 0812</span>
    </div>
  </div>

  <form class="contact-form">
    <div class="field" style="top:0"><label>Your Name:</label><span></span></div>
    <div class="field" style="top:30px"><label>Your Email:</label><span></span></div>
    <div class="field" style="top:60px"><label>Your Phone:</label><span></span></div>
    <div class="field message" style="top:90px"><label>Your Message:</label><span></span></div>
    <span class="btn-send" style="left:240px;top:155px;width:52px;height:17px">SEND</span>
  </form>
</section>

<footer class="site-footer">
  <span class="subscribe-label">Subscribe for newletter:</span>
  <span class="subscribe-input">Email address</span>
  <span class="btn-send" style="left:462px;top:10px;width:52px;height:17px;background:var(--orange-base)">SEND</span>
</footer>

</body>
</html>
```